Business Card *

A business card design
Use the logo uploaded in the brief page.
You may use placeholders in your design layouts.
I will provide the actual business card details to the winning designer.

Logo
Place for contact info (name, title, phone, email, etc)

Requirements
Must have
• Logo

```html
<!DOCTYPE html>
<html lang="en">
<head>
<meta charset="utf-8">
<title>Northfield Agriculture and Industry – Business Card</title>
<link rel="stylesheet" href="https://fonts.googleapis.com/css2?family=Archivo+Black&family=Roboto:wght@400;500&display=swap">
<style>
  :root {
    --backdrop: #3b3b3b;
    --card: #1d1d1d;
    --steel: #a9a9a9;
    --leaf: #2fb53a;
    --text: #e6e6e6;
  }
  * { margin: 0; padding: 0; box-sizing: border-box; }
  html, body { width: 799px; height: 1200px; overflow: hidden; }
  body {
    background: var(--backdrop);
    font-family: "Roboto", Arial, sans-serif;
    position: relative;
  }
  .card {
    position: absolute;
    left: 90px;
    width: 620px;
    height: 360px;
    background: var(--card);
    border-radius: 6px;
    box-shadow: 0 10px 24px rgba(0,0,0,.45);
    overflow: hidden;
  }
  .card--front { top: 120px; }
  .card--back { top: 700px; }

  /* Front face */
  .front-brand {
    position: absolute;
    inset: 0;
    display: flex;
    flex-direction: column;
    align-items: center;
    justify-content: center;
    gap: 22px;
  }
  .brand-dot {
    width: 120px;
    height: 120px;
    border-radius: 50%;
    border: 14px solid var(--steel);
  }
  .brand-name {
    font-family: "Archivo Black", Arial, sans-serif;
    color: var(--steel);
    text-transform: uppercase;
    text-align: center;
    line-height: 1;
  }
  .front-brand .brand-name { font-size: 40px; }
  .front-brand .brand-name small {
    display: block;
    font-size: 15px;
    letter-spacing: 2.4px;
    margin-top: 6px;
  }

  /* Back face */
  .back-mark {
    position: absolute;
    left: -40px;
    top: 20px;
    width: 300px;
    height: 300px;
    border-radius: 50%;
    border: 26px solid var(--steel);
  }
  .back-info {
    position: absolute;
    right: 34px;
    top: 44px;
    text-align: right;
  }
  .back-info .brand-name { font-size: 40px; }
  .back-info .brand-name small {
    display: block;
    font-size: 14.5px;
    letter-spacing: 2.3px;
    margin-top: 4px;
  }
  .person-name {
    margin-top: 36px;
    font-family: "Archivo Black", Arial, sans-serif;
    color: var(--leaf);
    font-size: 23px;
    text-transform: uppercase;
  }
  .person-role { color: var(--text); font-size: 16px; margin-top: 2px; }
  .address { color: var(--text); font-size: 16px; line-height: 1.3; margin-top: 14px; }
  .contact-list { list-style: none; margin-top: 12px; }
  .contact-list li {
    color: var(--text);
    font-size: 16px;
    line-height: 1.55;
    display: flex;
    justify-content: flex-end;
    align-items: center;
    gap: 10px;
  }
  .contact-list svg { width: 16px; height: 16px; fill: var(--leaf); }
</style>
</head>
<body>
  <section class="card card--front">
    <div class="front-brand">
      <div class="brand-dot"></div>
      <div class="brand-name">Northfield<small>Agriculture and Industry</small></div>
    </div>
  </section>

  <section class="card card--back">
    <div class="back-mark"></div>
    <div class="back-info">
      <div class="brand-name">Northfield<small>Agriculture and Industry</small></div>
      <p class="person-name">Dana R Miller</p>
      <p class="person-role">Managing Director</p>
      <p class="address">58 Orchard Lane, Any City,<br>Any Town, US 123456</p>
      <ul class="contact-list">
        <li>555-014-2200
          <svg viewBox="0 0 16 16" aria-hidden="true"><path d="M3 1h3l1.5 4-2 1.2a8 8 0 0 0 4.3 4.3l1.2-2 4 1.5v3c0 1-1 2-2 2A13 13 0 0 1 1 3c0-1 1-2 2-2z"/></svg>
        </li>
        <li>dana@northfield.com
          <svg viewBox="0 0 16 16" aria-hidden="true"><path d="M1 3h14v10H1z M2 4l6 5 6-5" fill="none" stroke="#2fb53a" stroke-width="1.6"/></svg>
        </li>
        <li>www.northfield.com
          <svg viewBox="0 0 16 16" aria-hidden="true"><circle cx="8" cy="8" r="7"/><path d="M1 8h14M8 1c3 3 3 11 0 14M8 1c-3 3-3 11 0 14" fill="none" stroke="#1d1d1d" stroke-width="1"/></svg>
        </li>
      </ul>
    </div>
  </section>
</body>
</html>
```